Meridian Sound Wellness LLC Card Design

Need business card with a logo for a hearing aid sales and audiology business. We have two Hearing Instrument Specialists and one Audiologist on staff. Over 25 years in business. Locally owned and operated. Financing available. Most insurances accepted.

Meridian Sound Wellness LLC
48730 W Linden Row, Suite 9
Spokane, WA 99481
509-617-2085
www.meridiansoundnorth.example

Manager
Tobias Wrenfield HIS COHC
License #81729046

Target Market(s)

50yr old + people with a hearing loss.

Industry/Entity Type

Business

Contact Information for Business Card

48730 W Linden Row, Suite 9
Spokane, WA 99481
509-617-2085
www.meridiansoundnorth.example

Manager
Tobias Wrenfield HIS COHC
NRPL #81729046

Font styles to use
Serif
Sans Serif

Requirements
Must have
• Business name, Tobias's name and title(s) and contact information, License #, web address
Nice to have
Should not have

```html
<!DOCTYPE html>
<html lang="en">
<head>
<meta charset="utf-8">
<title>Meridian Sound Wellness LLC – Business Card</title>
<link rel="stylesheet" href="https://fonts.googleapis.com/css2?family=Ubuntu:ital,wght@0,400;0,700;1,700&family=Exo+2:wght@400&display=swap">
<style>
  :root {
    --backdrop: #ebe7e1;
    --card: #ffffff;
    --gold: #c9962c;
    --brown: #855a26;
    --ink: #6b4a1f;
    --white: #ffffff;
  }
  html, body {
    margin: 0;
    width: 1200px;
    height: 813px;
    overflow: hidden;
    background: var(--backdrop);
  }
  .card {
    position: absolute;
    left: 40px;
    top: 88px;
    width: 1076px;
    height: 613px;
    background: var(--card);
    transform: scale(1.041);
    transform-origin: 0 0;
    overflow: hidden;
    box-shadow: 0 6px 18px rgba(0,0,0,0.18);
    font-family: "Ubuntu", sans-serif;
  }
  .bands { position: absolute; inset: 0; }
  .brand {
    position: absolute;
    left: 54px;
    top: 96px;
    margin: 0;
    font-family: "Ubuntu", sans-serif;
    font-weight: 700;
    font-size: 37px;
    color: var(--ink);
    white-space: nowrap;
  }
  .brand-dot {
    position: absolute;
    left: 652px;
    top: 88px;
    width: 62px;
    height: 62px;
    border-radius: 50%;
    background: var(--gold);
  }
  .person {
    position: absolute;
    right: 92px;
    top: 360px;
    text-align: center;
  }
  .person-name {
    display: block;
    font-size: 34px;
    color: var(--ink);
    white-space: nowrap;
    line-height: 44px;
  }
  .person-role {
    display: block;
    font-size: 29px;
    color: var(--gold);
    line-height: 34px;
  }
  .person-license {
    display: block;
    font-size: 23px;
    font-weight: 700;
    font-style: italic;
    color: var(--gold);
    line-height: 32px;
  }
  .person-icon {
    position: absolute;
    left: 997px;
    top: 358px;
    width: 50px;
    height: 50px;
  }
  .contact {
    position: absolute;
    left: 54px;
    top: 484px;
    margin: 0;
    padding: 0;
    list-style: none;
    font-family: "Exo 2", sans-serif;
    font-size: 27px;
    color: var(--white);
  }
  .contact li {
    display: flex;
    align-items: center;
    height: 35px;
    white-space: nowrap;
  }
  .contact svg { width: 32px; height: 28px; margin-right: 14px; flex: none; }
  .address {
    position: absolute;
    right: 36px;
    top: 490px;
    margin: 0;
    font-style: normal;
    text-align: right;
    font-size: 28px;
    line-height: 29px;
    color: var(--white);
  }
</style>
</head>
<body>
  <div class="card">
    <svg class="bands" viewBox="0 0 1076 613" aria-hidden="true">
      <polygon points="0,460 572,460 680,613 0,613" fill="var(--gold)"/>
      <polygon points="610,483 1076,483 1076,613 700,613" fill="var(--brown)"/>
    </svg>

    <h1 class="brand">Meridian Sound Wellness LLC</h1>
    <span class="brand-dot" aria-hidden="true"></span>

    <div class="person">
      <span class="person-name">Tobias Wrenfield HIS COHC</span>
      <span class="person-role">Manager</span>
      <span class="person-license">NRPL #81729046</span>
    </div>
    <svg class="person-icon" viewBox="0 0 50 50" aria-hidden="true">
      <circle cx="25" cy="25" r="25" fill="var(--gold)"/>
      <circle cx="25" cy="16" r="6" fill="var(--white)"/>
      <path d="M14 38 v-8 a11 9 0 0 1 22 0 v8 z" fill="var(--white)"/>
    </svg>

    <ul class="contact">
      <li>
        <svg viewBox="0 0 32 28" aria-hidden="true"><circle cx="16" cy="14" r="13" fill="var(--brown)"/><path d="M11 8 l3 -1 l2 4 l-2 2 q1 3 4 4 l2 -2 l4 2 l-1 3 q-9 1 -12 -12z" fill="var(--gold)"/></svg>
        509-617-2085
      </li>
      <li>
        <svg viewBox="0 0 32 28" aria-hidden="true"><rect x="3" y="7" width="26" height="16" fill="var(--brown)"/><path d="M3 7 l13 9 l13 -9" fill="none" stroke="var(--gold)" stroke-width="2"/></svg>
        hello@meridiansoundnorth.example
      </li>
      <li>
        <svg viewBox="0 0 32 28" aria-hidden="true"><g fill="none" stroke="var(--brown)" stroke-width="2"><circle cx="16" cy="14" r="12"/><ellipse cx="16" cy="14" rx="5" ry="12"/><path d="M4 14 h24 M6 8 h20 M6 20 h20"/></g></svg>
        www.meridiansoundnorth.example
      </li>
    </ul>

    <address class="address">
      48730 W Linden Row<br>
      Suite 9<br>
      Spokane, WA 99481
    </address>
  </div>
</body>
</html>
```